Awesome Professional Template for a collaborative report

File format: A4 PDF ideally

Design Requirements:

3 or 4 variants of a template some with graphics and pull quotes and a bio page for the essayists with a profile pic and a short descriptor

Layout Format: PPT would be perfect ideally portrait format

Style/Reference Guide: Varnholt or QM styles thought leadership reports as a guide

We need to input 10 essays around a specific subject with a nice layout with place holders for high impact pull quotes from the copy, stunning colourway and typrography probably A4 format but emailed as a PDF ideally not a huge file size. Striking front cover with title and list of contributors plus layout variations for the essays which will include a head shot short profile and contacts for the authors. Ideally a portrait format PPT that is easy to work with.

Target Market(s)

business professionals in brands

Industry/Entity Type

brand marketing

Font styles to use
Sans Serif

Colors
0054AA
0677BA
7BADD7
CADEEF
E8F1F8
00AB8E
00BBA5
67D7C9
C6EFE9
E9F9F6
F0912C
F2A743
F7CA91
FBE8D2
FDF5EE
6B429C
8869AF
B7A5CE
E3DAEB
F3F0F8

Requirements
Must have
• awesome visual impact

```html
<!DOCTYPE html>
<html lang="en">
<head>
<meta charset="utf-8">
<title>The Truth About AI – Report Template</title>
<link href="https://fonts.googleapis.com/css2?family=Lato:wght@400;700;900&display=swap" rel="stylesheet">
<style>
:root{
  --ink:#0f3426;
  --sage:#93a88a;
  --sage-soft:#b9c8b1;
  --mist:#e7e9e4;
  --text:#2a2f2c;
  --canvas:#eeefee;
  --paper:#ffffff;
  --rule:#cfd3cd;
}
*{margin:0;padding:0;box-sizing:border-box}
html,body{width:1200px;height:2400px;overflow:hidden;background:var(--canvas)}
body{font-family:"Lato",sans-serif;color:var(--text)}
.spread{position:absolute;left:0;width:1200px;height:574px;display:flex;gap:1px;background:var(--canvas)}
.row-1{top:13px}.row-2{top:612px}.row-3{top:1211px}.row-4{top:1812px}
.page{position:relative;width:400px;height:574px;background:var(--paper);overflow:hidden}
.abs{position:absolute}
.cover-title{font-weight:900;font-size:58px;line-height:62px;color:var(--ink);letter-spacing:-.5px}
.cover-title span{display:block;color:var(--sage)}
.dot{position:absolute;width:48px;height:48px;border-radius:50%;background:var(--mist)}
.visual{position:absolute}
.visual-head{background:radial-gradient(ellipse at 55% 45%,#9cbf84 0%,#c9dcbb 35%,rgba(236,242,232,.6) 65%,rgba(255,255,255,0) 85%)}
.visual-mind{background:radial-gradient(ellipse at 40% 55%,#7fa86a 0%,#b7cfa6 35%,#e3ecdc 62%,rgba(255,255,255,0) 88%)}
.corner-web{position:absolute;right:0;bottom:0;width:170px;height:120px;background:radial-gradient(ellipse at 90% 100%,rgba(150,190,150,.55) 0%,rgba(200,222,200,.35) 40%,rgba(255,255,255,0) 75%)}
.corner-web.wide{width:260px;height:260px}
.chapter-badge{left:36px;top:18px;width:80px;height:80px;background:var(--sage);color:#fff;font-weight:700;font-size:38px;display:flex;align-items:center;justify-content:center}
.essay-title{left:39px;top:134px;font-weight:900;font-size:45px;line-height:54px;color:var(--ink)}
.portrait{left:42px;top:336px;width:87px;height:87px;border-radius:50%;background:var(--mist)}
.author-name{left:46px;top:430px;font-weight:700;font-size:14px;color:var(--ink)}
.author-role{left:24px;top:453px;width:121px;height:17px;background:var(--sage);color:#fff;font-size:10px;line-height:17px;text-align:center}
.author-bio{left:24px;top:482px;width:272px;font-size:8px;line-height:12px}
.page-title{left:36px;top:42px;font-weight:900;font-size:31px;color:var(--ink)}
.toc{left:37px;top:108px;width:320px;list-style:none}
.toc li{display:flex;align-items:center;height:31.8px;border-bottom:1px solid var(--rule);font-size:10.5px}
.toc li:last-child{border-bottom:none}
.toc .num{width:52px;padding-left:5px;color:var(--sage);font-size:13px}
.toc .name{flex:1;font-weight:700;color:#111}
.toc .pg{font-size:10px;color:#111}
.body{font-size:7.4px;line-height:11.3px;overflow:hidden}
.body p{margin-bottom:8px}
.body.indent p{text-indent:12px;margin-bottom:7px}
.box{position:absolute;background:var(--mist)}
.subhead{position:absolute;font-size:11.5px;color:var(--sage);font-weight:700}
.pull-quote{left:206px;top:26px;width:180px;font-size:12.2px;line-height:21.4px;color:var(--sage);letter-spacing:.3px}
.footer-rule{position:absolute;left:14px;top:556px;width:316px;height:1px;background:#9aa09a}
.footer-text{position:absolute;left:16px;top:562px;font-size:5.2px;letter-spacing:.9px;color:#333}
.folio{position:absolute;left:370px;top:555px;width:15px;height:15px;border-radius:50%;background:var(--ink);color:#fff;font-size:6px;line-height:15px;text-align:center}
</style>
</head>
<body>

<!-- Row 1: covers and essay opener -->
<section class="spread row-1">
  <article class="page">
    <h1 class="abs cover-title" style="left:40px;top:80px">The Truth<span>About AI</span></h1>
    <div class="dot" style="left:40px;top:262px"></div><div class="dot" style="left:97px;top:262px"></div><div class="dot" style="left:154px;top:262px"></div>
    <div class="dot" style="left:40px;top:326px"></div><div class="dot" style="left:97px;top:326px"></div><div class="dot" style="left:154px;top:326px"></div>
    <div class="dot" style="left:40px;top:391px"></div><div class="dot" style="left:97px;top:391px"></div><div class="dot" style="left:154px;top:391px"></div>
    <div class="dot" style="left:40px;top:456px"></div><div class="dot" style="left:97px;top:456px"></div><div class="dot" style="left:154px;top:456px"></div>
    <div class="visual visual-head" role="img" aria-label="Green-toned illustration of a digital human head profile with molecular structures" style="left:200px;top:310px;width:220px;height:264px"></div>
  </article>
  <article class="page">
    <h1 class="abs cover-title" style="left:73px;top:80px">The Truth<span>About AI</span></h1>
    <div class="visual visual-mind" role="img" aria-label="Green-toned illustration of a human head silhouette filled with circuitry and mathematical formulas" style="left:60px;top:300px;width:340px;height:274px"></div>
  </article>
  <article class="page">
    <div class="abs chapter-badge">01</div>
    <h2 class="abs essay-title">Title of The<br>Essay Goes<br>Here</h2>
    <div class="corner-web wide" role="img" aria-label="Faint green network of connected dots"></div>
    <div class="abs portrait" role="img" aria-label="Author profile photo"></div>
    <p class="abs author-name">Author name</p>
    <p class="abs author-role">Title Here</p>
    <p class="abs author-bio">Cras condimentum varius tellus sit amet tristique. Aliquam varius tortor vel nisl efficitur, non tempus nisl porttitor. Phasellus porttitor turpis at efficitur convallis. Etiam at viverra lectus. Etiam gravida nisi eu tellus sollicitudin tristique. Proin finibus</p>
  </article>
</section>

<!-- Row 2: contents, introduction, text page -->
<section class="spread row-2">
  <article class="page">
    <h2 class="abs page-title" style="top:48px">Contents</h2>
    <ol class="abs toc">
      <li><span class="num">01</span><span class="name">Chapter Title</span><span class="pg">1</span></li>
      <li><span class="num">02</span><span class="name">Chapter Title</span><span class="pg">2</span></li>
      <li><span class="num">03</span><span class="name">Chapter Title</span><span class="pg">3</span></li>
      <li><span class="num">04</span><span class="name">Chapter Title</span><span class="pg">4</span></li>
      <li><span class="num">05</span><span class="name">Chapter Title</span><span class="pg">5</span></li>
      <li><span class="num">06</span><span class="name">Chapter Title</span><span class="pg">6</span></li>
      <li><span class="num">07</span><span class="name">Chapter Title</span><span class="pg">7</span></li>
      <li><span class="num">08</span><span class="name">Chapter Title</span><span class="pg">8</span></li>
      <li><span class="num">09</span><span class="name">Chapter Title</span><span class="pg">9</span></li>
      <li><span class="num">10</span><span class="name">Chapter Title</span><span class="pg">10</span></li>
      <li><span class="num">11</span><span class="name">Chapter Title</span><span class="pg">11</span></li>
      <li><span class="num">12</span><span class="name">Chapter Title</span><span class="pg">12</span></li>
    </ol>
    <div class="corner-web" role="img" aria-label="Faint green network of connected dots"></div>
    <div class="footer-rule"></div><p class="footer-text">Copyright © 2023 Kestrel | The Truth about AI</p><span class="folio">4</span>
  </article>
  <article class="page">
    <h2 class="abs page-title" style="left:38px">Introduction</h2>
    <div class="abs body" style="left:38px;top:100px;width:210px;height:430px">
      <p>Cras condimentum varius tellus sit amet tristique. Aliquam varius tortor vel nisl efficitur, non tempus nisl porttitor. Phasellus porttitor turpis at efficitur convallis. Etiam at viverra lectus. Etiam gravida nisi eu tellus sollicitudin tristique. Proin finibus quam eu finibus hendrerit. Suspendisse vel magna non sem sollicitudin consectetur vitae rutrum nibh. Nunc quis nisi vitae lectus porttitor ornare eu nec lorem. Aenean blandit mauris vitae varius mollis. Pellentesque hendrerit enim sed commodo venenatis. Morbi turpis elit, fringilla ac laoreet a, rutrum sed ex. Nunc nec lorem ante. Sed eu tellus sed mauris</p>
      <p>Cras condimentum varius tellus sit amet tristique. Aliquam varius tortor vel nisl efficitur, non tempus nisl porttitor. Phasellus porttitor turpis at efficitur convallis. Etiam at viverra lectus. Etiam gravida nisi eu tellus sollicitudin tristique. Proin finibus quam eu finibus hendrerit. Suspendisse vel magna non sem sollicitudin consectetur vitae rutrum nibh. Nunc quis nisi vitae lectus porttitor ornare eu nec lorem. Aenean blandit mauris vitae varius mollis. Pellentesque hendrerit enim sed commodo venenatis. Morbi turpis elit, fringilla ac laoreet a, rutrum sed ex. Nunc nec lorem ante. Sed eu tellus sed mauris</p>
      <p>Cras condimentum varius tellus sit amet tristique. Aliquam varius tortor vel nisl efficitur, non tempus nisl porttitor. Phasellus porttitor turpis at efficitur convallis. Etiam at viverra lectus. Etiam gravida nisi eu tellus sollicitudin tristique. Proin finibus quam eu finibus hendrerit. Suspendisse vel magna non sem sollicitudin consectetur vitae rutrum nibh. Nunc quis nisi vitae lectus porttitor ornare eu nec lorem. Aenean blandit mauris vitae varius mollis. Pellentesque hendrerit enim sed commodo venenatis. Morbi turpis elit, fringilla ac laoreet a, rutrum sed ex. Nunc nec lorem ante. Sed eu tellus sed mauris</p>
    </div>
    <div class="box" role="img" aria-label="Image placeholder" style="left:269px;top:100px;width:131px;height:396px"></div>
    <div class="corner-web" role="img" aria-label="Faint green network of connected dots"></div>
    <div class="footer-rule"></div><p class="footer-text">Copyright © 2023 Kestrel | The Truth about AI</p><span class="folio">5</span>
  </article>
  <article class="page">
    <h2 class="abs page-title">Title Here</h2>
    <div class="abs body indent" style="left:39px;top:100px;width:322px;height:420px">
      <p>Curabitur facilisis vitae est id pulvinar. Duis aliquet nulla consequat est malesuada luctus. Vestibulum eu nisl est. Cras vel velit dictum, feugiat magna vel, efficitur mauris. Proin quis lectus risus. Suspendisse maximus, leo vulputate pellentesque rutrum, ex dolor sodales nisi, eget convallis sapien ipsum quis arcu. Fusce maximus, nunc quis fringilla fermentum, massa tellus pellentesque tortor, eget scelerisque nibh nunc non felis. Quisque ut varius quam. Vivamus lobortis venenatis purus a semper. Curabitur quis tortor eros. Maecenas ac finibus tellus, sed tempus ligula. Cras quis mi ullamcorper, congue lectus sit amet, semper tellus.</p>
      <p>Cras condimentum varius tellus sit amet tristique. Aliquam varius tortor vel nisl efficitur, non tempus nisl porttitor. Phasellus porttitor turpis at efficitur convallis. Etiam at viverra lectus. Etiam gravida nisi eu tellus sollicitudin tristique. Proin finibus quam eu finibus hendrerit. Suspendisse vel magna non sem sollicitudin consectetur vitae rutrum nibh. Nunc quis nisi vitae lectus porttitor ornare eu nec lorem. Aenean blandit mauris vitae varius mollis. Pellentesque hendrerit enim sed commodo venenatis. Morbi turpis elit, fringilla ac laoreet a, rutrum sed ex. Nunc nec lorem ante. Sed eu tellus sed mauris hendrerit pretium.</p>
      <p>Phasellus quis massa dapibus, vulputate ex non, ultrices magna. Maecenas dignissim elit nec massa dapibus, vel aliquam nulla maximus. Cras ac est dapibus, ornare elit a, convallis elit. Etiam et diam in felis laoreet lacinia. Ullamcorper, congue lectus sit amet, semper tellus. Cras ac est dapibus, ornare elit a, convallis elit. Etiam et diam in felis laoreet lacinia. Cras ac est dapibus, ornare elit a, convallis elit. Etiam et diam in felis laoreet lacinia. Ullamcorper, congue lectus sit amet, semper tellus. Cras ac est dapibus, ornare elit a, convallis elit. Etiam et diam in felis laoreet lacinia.</p>
      <p>Cras condimentum varius tellus sit amet tristique. Aliquam varius tortor vel nisl efficitur, non tempus nisl porttitor. Phasellus porttitor turpis at efficitur convallis. Etiam at viverra lectus. Etiam gravida nisi eu tellus sollicitudin tristique. Proin finibus quam eu finibus hendrerit. Suspendisse vel magna non sem sollicitudin consectetur vitae rutrum nibh. Nunc quis nisi vitae lectus porttitor ornare eu nec lorem. Aenean blandit mauris vitae varius mollis. Pellentesque hendrerit enim sed commodo venenatis. Morbi turpis elit, fringilla ac laoreet a, rutrum sed ex. Nunc nec lorem ante. Sed eu tellus sed mauris hendrerit pretium.</p>
    </div>
    <div class="corner-web" role="img" aria-label="Faint green network of connected dots"></div>
    <div class="footer-rule"></div><p class="footer-text">Copyright © 2023 Kestrel | The Truth about AI</p><span class="folio">6</span>
  </article>
</section>

<!-- Row 3: pull quote and column variants -->
<section class="spread row-3">
  <article class="page">
    <div class="box" role="img" aria-label="Image placeholder" style="left:0;top:0;width:186px;height:200px"></div>
    <blockquote class="abs pull-quote">"Lorem ipsum dolor sit amet, consectetur adipiscing elit. Nullam imperdiet mi vitae ipsum elementum, sollicitudin congue mi pretium Nullam imperdiet mi vitae ipsum elementum, sollicitudin ".</blockquote>
    <div class="abs body" style="left:35px;top:228px;width:145px;height:322px">
      <p>Curabitur facilisis vitae est id pulvinar. Duis aliquet nulla consequat est malesuada luctus. Vestibulum eu nisl est. Cras vel velit dictum, feugiat magna vel, efficitur mauris. Proin quis lectus risus. Suspendisse maximus, leo vulputate pellentesque rutrum, ex dolor sodales nisi, eget convallis sapien ipsum quis arcu. Fusce maximus, nunc quis fringilla fermentum, massa tellus pellentesque tortor, eget scelerisque nibh nunc non felis. Quisque ut varius quam. Vivamus lobortis venenatis purus a semper.</p>
      <p>Curabitur facilisis vitae est id pulvinar. Duis aliquet nulla consequat est malesuada luctus. Vestibulum eu nisl est. Cras vel velit dictum, feugiat magna vel, efficitur mauris. Proin quis lectus risus. Suspendisse maximus, leo vulputate pellentesque rutrum, ex dolor sodales nisi, eget convallis sapien ipsum quis arcu. Fusce maximus, nunc quis fringilla fermentum, massa tellus pellentesque tortor, eget scelerisque nibh nunc non felis. Quisque ut varius quam. Vivamus</p>
    </div>
    <div class="abs body" style="left:204px;top:228px;width:124px;height:322px">
      <p>Cras condimentum varius tellus sit amet tristique. Aliquam varius tortor vel nisl efficitur, non tempus nisl porttitor. Phasellus porttitor turpis at efficitur convallis. Etiam at viverra lectus. Etiam gravida nisi eu tellus sollicitudin tristique. Proin finibus quam eu finibus hendrerit. Suspendisse vel magna non sem sollicitudin consectetur vitae rutrum nibh. Nunc quis nisi vitae lectus porttitor ornare eu nec lorem.</p>
      <p>Cras ac est dapibus, ornare elit a, convallis elit. Etiam et diam in felis laoreet lacinia. Aenean blandit mauris vitae varius mollis. Pellentesque hendrerit eni. Cras ac est dapibus, ornare elit a, convallis elit. Etiam et diam in felis laoreet lacinia. Aenean blandit mauris vitae varius mollis. Pellentesque hendrerit eni. Aenean blandit</p>
    </div>
    <div class="box" role="img" aria-label="Image placeholder" style="left:341px;top:253px;width:59px;height:214px"></div>
    <div class="corner-web" role="img" aria-label="Faint green network of connected dots"></div>
    <div class="footer-rule"></div><p class="footer-text">Copyright © 2023 Kestrel | The Truth about AI</p><span class="folio">7</span>
  </article>
  <article class="page">
    <h3 class="subhead" style="left:40px;top:50px">Sub-Heading</h3>
    <div class="abs body" style="left:40px;top:84px;width:146px;height:450px">
      <p>Cras condimentum varius tellus sit amet tristique. Aliquam varius tortor vel nisl efficitur, non tempus nisl porttitor. Phasellus porttitor turpis at efficitur convallis. Etiam at viverra lectus. Etiam gravida nisi eu tellus sollicitudin tristique. Proin finibus quam eu finibus hendrerit. Suspendisse vel magna non sem sollicitudin consectetur vitae rutrum nibh. Nunc quis nisi vitae lectus porttitor ornare eu nec lorem. Aenean blandit mauris vitae varius mollis. Pellentesque hendrerit enim sed commodo venenatis. Morbi turpis elit, fringilla ac laoreet a, rutrum sed ex. Nunc nec lorem ante. Sed eu tellus sed mauris hendrerit pretium. Phasellus quis massa dapibus, vulputate ex non, ultrices magna. Maecenas dignissim elit nec massa dapibus, vel aliquam nulla maximus.</p>
      <p>Cras condimentum varius tellus sit amet tristique. Aliquam varius tortor vel nisl efficitur, non tempus nisl porttitor. Phasellus porttitor turpis at efficitur convallis. Etiam at viverra lectus. Etiam gravida nisi eu tellus sollicitudin tristique. Proin finibus</p>
      <p>Cras condimentum varius tellus sit amet tristique. Aliquam varius tortor vel nisl efficitur, non tempus nisl porttitor. Phasellus porttitor turpis at efficitur convallis. Etiam at viverra</p>
    </div>
    <div class="abs body" style="left:200px;top:84px;width:178px;height:200px">
      <p>Curabitur facilisis vitae est id pulvinar. Duis aliquet nulla consequat est malesuada luctus. Vestibulum eu nisl est. Cras vel velit dictum, feugiat magna vel, efficitur mauris. Proin quis lectus risus. Suspendisse maximus, leo vulputate pellentesque rutrum, ex dolor sodales nisi, eget convallis sapien ipsum quis arcu. Fusce maximus, nunc quis fringilla fermentum, massa tellus pellentesque tortor, eget scelerisque nibh nunc non felis. Quisque ut varius quam. Vivamus lobortis venenatis purus a semper. Curabitur quis tortor eros. Maecenas ac finibus tellus, sed tempus ligula. Cras quis mi ullamcorper, congue lectus sit amet, semper tellus. Cras ac est dapibus, ornare elit a, convallis elit. Etiam et diam in felis laoreet lacinia. Ullamcorper, congue lectus sit</p>
    </div>
    <div class="box" role="img" aria-label="Image placeholder" style="left:219px;top:317px;width:158px;height:168px"></div>
    <div class="corner-web" role="img" aria-label="Faint green network of connected dots"></div>
    <div class="footer-rule"></div><p class="footer-text">Copyright © 2023 Kestrel | The Truth about AI</p><span class="folio">8</span>
  </article>
  <article class="page">
    <div class="box" role="img" aria-label="Image placeholder" style="left:0;top:0;width:283px;height:65px"></div>
    <h3 class="subhead" style="left:39px;top:132px">Sub-Heading</h3>
    <div class="abs body" style="left:42px;top:155px;width:142px;height:275px">
      <p>Phasellus porttitor turpis at efficitur convallis. Etiam at viverra lectus. Etiam gravida nisi eu tellus sollicitudin tristique. Pellentesque hendrerit enim sed commodo venenatis. Morbi turpis elit, fringilla ac laoreet a, rutrum sed ex. Nunc nec lorem ante. Sed eu tellus sed mauris hendrerit pretium. Phasellus quis massa dapibus, vulputate ex non, ultrices magna.</p>
      <p>Maecenas dignissim elit nec massa dapibus, vel aliquam nulla maximus. Nunc quis nisi vitae lectus porttitor ornare eu nec lorem. Aenean blandit mauris vitae varius mollis. Pellentesque hendrerit enim sed commodo venenatis. Morbi turpis elit, fringilla ac laoreet a, rutrum sed ex. Nunc nec lorem ante. Sed eu tellus sed mauris hendrerit pretium. Phasellus quis massa dapibus, vulputate ex non,</p>
    </div>
    <h3 class="subhead" style="left:39px;top:455px">Sub-Heading</h3>
    <div class="abs body" style="left:42px;top:478px;width:142px;height:60px">
      <p>Phasellus porttitor turpis at efficitur convallis. Etiam at viverra lectus. Etiam gravida nisi eu tellus sollicitudin tristique. Pellentesque hendrerit enim sed commodo venenatis.</p>
    </div>
    <div class="abs body" style="left:216px;top:106px;width:156px;height:432px">
      <p>Phasellus porttitor turpis at efficitur convallis. Etiam at viverra lectus. Etiam gravida nisi eu tellus sollicitudin tristique. Pellentesque hendrerit enim sed commodo venenatis. Morbi turpis elit, fringilla ac laoreet a, rutrum sed ex. Nunc nec lorem ante. Sed eu tellus sed mauris hendrerit pretium. Phasellus quis massa dapibus, vulputate ex non, ultrices magna.</p>
      <p>Maecenas dignissim elit nec massa dapibus, vel aliquam nulla maximus. Nunc quis nisi vitae lectus porttitor ornare eu nec lorem. Aenean blandit mauris vitae varius mollis. Pellentesque hendrerit enim sed commodo venenatis. Morbi turpis elit, fringilla ac laoreet a, rutrum sed ex. Nunc nec lorem ante. Sed eu tellus sed mauris hendrerit pretium. Phasellus quis massa dapibus, vulputate ex non, ultrices magna. Maecenas dignissim elit nec massa dapibus, vel aliquam nulla maximus.</p>
      <p>Maecenas dignissim elit nec massa dapibus, vel aliquam nulla maximus. Nunc quis nisi vitae lectus porttitor ornare eu nec lorem. Aenean blandit mauris vitae varius mollis. Pellentesque hendrerit enim sed commodo venenatis. Morbi turpis elit, fringilla ac laoreet a, rutrum sed ex. Nunc nec lorem ante. Sed eu tellus sed mauris hendrerit pretium. Phasellus quis massa dapibus, vulputate ex non, ultrices magna. Maecenas dignissim elit nec massa dapibus, vel aliquam nulla maximus.</p>
    </div>
    <div class="corner-web" role="img" aria-label="Faint green network of connected dots"></div>
    <div class="footer-rule"></div><p class="footer-text">Copyright © 2023 Kestrel | The Truth about AI</p><span class="folio">9</span>
  </article>
</section>

<!-- Row 4: further column variants -->
<section class="spread row-4">
  <article class="page">
    <h3 class="subhead" style="left:23px;top:40px">Sub-Heading</h3>
    <div class="abs body" style="left:23px;top:66px;width:165px;height:478px">
      <p>Cras condimentum varius tellus sit amet tristique. Aliquam varius tortor vel nisl efficitur, non tempus nisl porttitor. Phasellus porttitor turpis at efficitur convallis. Etiam at viverra lectus. Etiam gravida nisi eu tellus sollicitudin tristique. Proin finibus quam eu finibus hendrerit. Suspendisse vel magna non sem sollicitudin consectetur vitae rutrum nibh. Nunc quis nisi vitae lectus porttitor ornare eu nec lorem. Aenean blandit mauris vitae varius mollis.</p>
      <p>Morbi turpis elit, fringilla ac laoreet a, rutrum sed ex. Nunc nec lorem ante. Sed eu tellus sed mauris hendrerit pretium. Phasellus quis massa dapibus, vulputate ex non, ultrices magna. Maecenas dignissim elit nec massa dapibus, vel aliquam nulla maximus. Pellentesque hendrerit enim sed commodo venenatis. Morbi turpis elit, fringilla ac laoreet a, rutrum sed ex. Nunc nec lorem ante. Nunc quis nisi vitae lectus porttitor ornare eu nec lorem. Aenean blandit mauris vitae varius mollis. Pellentesque hendrerit enim sed commodo venenatis. Nunc quis nisi vitae lectus porttitor ornare eu nec lorem. Aenean blandit mauris vitae varius mollis. Aenean blandit mauris vitae varius mollis.</p>
      <p>Cras condimentum varius tellus sit amet tristique. Aliquam varius tortor vel nisl efficitur, non tempus nisl porttitor. Phasellus porttitor turpis at efficitur convallis. Etiam at viverra lectus. Etiam gravida nisi eu tellus sollicitudin tristique. Proin finibus quam eu finibus hendrerit. Suspendisse vel magna non sem sollicitudin consectetur vitae rutrum nibh. Nunc quis nisi vitae lectus porttitor ornare eu nec lorem. Aenean blandit mauris</p>
    </div>
    <div class="box" role="img" aria-label="Image placeholder" style="left:204px;top:31px;width:123px;height:284px"></div>
    <div class="box" role="img" aria-label="Image placeholder" style="left:350px;top:31px;width:50px;height:510px"></div>
    <h3 class="subhead" style="left:206px;top:332px">Sub-Heading</h3>
    <div class="abs body" style="left:209px;top:349px;width:120px;height:190px">
      <p>Aliquam varius tortor vel nisl efficitur, non tempus nisl porttitor. Phasellus porttitor turpis at efficitur convallis. Etiam at viverra lectus. Etiam gravida nisi eu tellus sollicitudin tristique. Proin finibus quam eu finibus hendrerit. Suspendisse vel magna non sem sollicitudin consectetur vitae rutrum nibh. Nunc quis nisi vitae lectus porttitor ornare eu nec lorem. Aenean blandit mauris vitae varius mollis. Pellentesque hendrerit enim sed commodo</p>
    </div>
    <div class="corner-web" role="img" aria-label="Faint green network of connected dots"></div>
    <div class="footer-rule"></div><p class="footer-text">Copyright © 2023 Kestrel | The Truth about AI</p><span class="folio">10</span>
  </article>
  <article class="page">
    <div class="box" role="img" aria-label="Image placeholder" style="left:0;top:0;width:400px;height:109px"></div>
    <h3 class="subhead" style="left:18px;top:136px">Sub-Heading</h3>
    <div class="abs body" style="left:23px;top:158px;width:165px;height:385px">
      <p>Cras condimentum varius tellus sit amet tristique. Aliquam varius tortor vel nisl efficitur, non tempus nisl porttitor. Phasellus porttitor turpis at efficitur convallis. Etiam at viverra lectus. Etiam gravida nisi eu tellus sollicitudin tristique. Proin finibus quam eu finibus hendrerit. Suspendisse vel magna non sem sollicitudin consectetur vitae rutrum nibh. Nunc quis nisi vitae lectus porttitor ornare eu nec lorem. Aenean blandit mauris vitae varius mollis.</p>
      <p>Morbi turpis elit, fringilla ac laoreet a, rutrum sed ex. Nunc nec lorem ante. Sed eu tellus sed mauris hendrerit pretium. Phasellus quis massa dapibus, vulputate ex non, ultrices magna. Maecenas dignissim elit nec massa dapibus, vel aliquam nulla maximus. Pellentesque hendrerit enim sed commodo venenatis. Morbi turpis elit, fringilla ac laoreet a, rutrum sed ex. Nunc nec lorem ante. Nunc quis nisi vitae lectus porttitor ornare eu nec lorem. Aenean blandit mauris vitae varius mollis. Pellentesque hendrerit enim sed commodo venenatis. Nunc quis nisi vitae lectus porttitor ornare eu nec lorem. Aenean blandit mauris vitae varius mollis. Aenean blandit mauris vitae varius mollis.</p>
      <p>Maecenas dignissim elit nec massa dapibus, vel aliquam nulla maximus. Nunc quis nisi</p>
    </div>
    <div class="abs body" style="left:213px;top:158px;width:165px;height:385px">
      <p>Cras condimentum varius tellus sit amet tristique. Aliquam varius tortor vel nisl efficitur, non tempus nisl porttitor. Phasellus porttitor turpis at efficitur convallis. Etiam at viverra lectus. Etiam gravida nisi eu tellus sollicitudin tristique. Proin finibus quam eu finibus hendrerit. Suspendisse vel magna non sem sollicitudin consectetur vitae rutrum nibh. Nunc quis nisi vitae lectus porttitor ornare eu nec lorem. Aenean blandit mauris vitae varius mollis.</p>
      <p>Morbi turpis elit, fringilla ac laoreet a, rutrum sed ex. Nunc nec lorem ante. Sed eu tellus sed mauris hendrerit pretium. Phasellus quis massa dapibus, vulputate ex non, ultrices magna. Maecenas dignissim elit nec massa dapibus, vel aliquam nulla maximus. Pellentesque hendrerit enim sed commodo venenatis. Morbi turpis elit, fringilla ac laoreet a, rutrum sed ex. Nunc nec lorem ante. Nunc quis nisi vitae lectus porttitor ornare eu nec lorem. Aenean blandit mauris vitae varius mollis. Pellentesque hendrerit enim sed commodo venenatis. Nunc quis nisi vitae lectus porttitor ornare eu nec lorem. Aenean blandit mauris vitae varius mollis. Aenean blandit mauris vitae varius mollis.</p>
      <p>Maecenas dignissim elit nec massa dapibus, vel aliquam nulla maximus. Nunc quis nisi vitae lectus porttitor ornare eu nec lorem.</p>
    </div>
    <div class="corner-web" role="img" aria-label="Faint green network of connected dots"></div>
    <div class="footer-rule"></div><p class="footer-text">Copyright © 2023 Kestrel | The Truth about AI</p><span class="folio">11</span>
  </article>
  <article class="page">
    <h3 class="subhead" style="left:24px;top:31px">Sub-Heading</h3>
    <div class="abs body" style="left:24px;top:50px;width:165px;height:490px">
      <p>Cras condimentum varius tellus sit amet tristique. Aliquam varius tortor vel nisl efficitur, non tempus nisl porttitor. Phasellus porttitor turpis at efficitur convallis. Etiam at viverra lectus. Etiam gravida nisi eu tellus sollicitudin tristique. Proin finibus quam eu finibus hendrerit. Suspendisse vel magna non sem sollicitudin consectetur vitae rutrum nibh. Nunc quis nisi vitae lectus porttitor ornare eu nec lorem. Aenean blandit mauris vitae varius mollis.</p>
      <p>Morbi turpis elit, fringilla ac laoreet a, rutrum sed ex. Nunc nec lorem ante. Sed eu tellus sed mauris hendrerit pretium. Phasellus quis massa dapibus, vulputate ex non, ultrices magna. Maecenas dignissim elit nec massa dapibus, vel aliquam nulla maximus. Pellentesque hendrerit enim sed commodo venenatis. Morbi turpis elit, fringilla ac laoreet a, rutrum sed ex. Nunc nec lorem ante. Nunc quis nisi vitae lectus porttitor ornare eu nec lorem. Aenean blandit mauris vitae varius mollis. Pellentesque hendrerit enim sed commodo venenatis. Nunc quis nisi vitae lectus porttitor ornare eu nec lorem. Aenean blandit mauris vitae varius mollis. Aenean blandit mauris vitae varius mollis.</p>
      <p>Morbi turpis elit, fringilla ac laoreet a, rutrum sed ex. Nunc nec lorem ante. Sed eu tellus sed mauris hendrerit pretium. Phasellus quis massa dapibus, vulputate ex non, ultrices magna. Maecenas dignissim elit nec massa dapibus, vel aliquam nulla maximus. Pellentesque hendrerit enim sed commodo venenatis. Morbi turpis elit, fringilla ac laoreet a, rutrum sed ex. Nunc nec lorem ante. Nunc quis nisi vitae lectus porttitor ornare eu nec lorem. Aenean blandit mauris</p>
    </div>
    <div class="abs body" style="left:214px;top:50px;width:165px;height:490px">
      <p>Cras condimentum varius tellus sit amet tristique. Aliquam varius tortor vel nisl efficitur, non tempus nisl porttitor. Phasellus porttitor turpis at efficitur convallis. Etiam at viverra lectus. Etiam gravida nisi eu tellus sollicitudin tristique. Proin finibus quam eu finibus hendrerit. Suspendisse vel magna non sem sollicitudin consectetur vitae rutrum nibh. Nunc quis nisi vitae lectus porttitor ornare eu nec lorem. Aenean blandit mauris vitae varius mollis.</p>
      <p>Morbi turpis elit, fringilla ac laoreet a, rutrum sed ex. Nunc nec lorem ante. Sed eu tellus sed mauris hendrerit pretium. Phasellus quis massa dapibus, vulputate ex non, ultrices magna. Maecenas dignissim elit nec massa dapibus, vel aliquam nulla maximus. Pellentesque hendrerit enim sed commodo venenatis. Morbi turpis elit, fringilla ac laoreet a, rutrum sed ex. Nunc nec lorem ante. Nunc quis nisi vitae lectus porttitor ornare eu nec lorem. Aenean blandit mauris vitae varius mollis. Pellentesque hendrerit enim sed commodo venenatis. Nunc quis nisi vitae lectus porttitor ornare eu nec lorem. Aenean blandit mauris vitae varius mollis. Aenean blandit mauris vitae varius mollis.</p>
      <p>Morbi turpis elit, fringilla ac laoreet a, rutrum sed ex. Nunc nec lorem ante. Sed eu tellus sed mauris hendrerit pretium. Phasellus quis massa dapibus, vulputate ex non, ultrices magna. Maecenas dignissim elit nec massa dapibus, vel aliquam nulla maximus. Pellentesque hendrerit enim sed commodo venenatis. Morbi turpis elit, fringilla ac laoreet a, rutrum sed ex. Nunc nec lorem ante. Nunc quis nisi vitae lectus porttitor ornare eu nec lorem. Aenean blandit mauris</p>
    </div>
    <div class="corner-web" role="img" aria-label="Faint green network of connected dots"></div>
    <div class="footer-rule"></div><p class="footer-text">Copyright © 2023 Kestrel | The Truth about AI</p><span class="folio">12</span>
  </article>
</section>

</body>
</html>
```